Editable Flyer Layout for MIDWAY SWIFTLINE

to come up with a flyer layout that has editable spots to change promotions from time to time. We are a courier company in Calgary Alberta. Our logos and color schemes can be viewed on our website www.routebrisker.com We are wanting something that fits with website but more of an edge on the print media side. Our website also feature our "Focus" page which will tell you about us and our practices. Please conside this when constructing flyer. We also have additional image files for you if needed.

Thanks !!!!
Updates

Some of these designs are great. Never expected to get so many different results. I will comment on potential designs once we have reviewed all and only after deadline. For now Thanks to all .....!!!!!

Thank you all for your submissions. Some have been eliminated. Those that have not I have sent message to you. The designs look great but need some minor changes. I have sent some suggestions and revert back to you. Please review the notes above on ad (promo) and the editable space.

Thanks Very Much !!!

Tam

Thank You all very much for your submissions. We will be choosing a candidate today. We love this service, you all did awesome.

Thanks
Tam

Target Market(s)

Commerical businesses shipping freight and courier packages.

Industry/Entity Type

It Company

Requirements
Must have
• Flyer must be free of copyright.

```html
<!DOCTYPE html>
<html lang="en">
<head>
<meta charset="utf-8">
<title>MIDWAY SWIFTLINE – Flyer</title>
<link href="https://fonts.googleapis.com/css2?family=Arimo:ital,wght@0,400;0,700;1,400;1,700&family=Roboto+Condensed:ital,wght@0,700;1,700;1,800&display=swap" rel="stylesheet">
<style>
  :root {
    --blue-deep: #0b3f8f;
    --blue: #1565c0;
    --blue-bright: #2a8ee0;
    --red: #d8121b;
    --red-dark: #9c0a10;
    --ink: #1a1a1a;
    --paper: #f4f5f7;
    --grey: #b9bec6;
    --white: #ffffff;
  }
  * { box-sizing: border-box; margin: 0; padding: 0; }
  html, body { width: 849px; height: 1200px; overflow: hidden; background: var(--white); }
  .flyer {
    position: relative; width: 849px; height: 1200px; overflow: hidden;
    background: var(--paper);
    font-family: "Arimo", Arial, sans-serif; color: var(--ink);
  }

  /* header */
  .header {
    position: absolute; left: 0; top: 0; width: 100%; height: 125px;
    background: linear-gradient(100deg, var(--blue-deep) 0%, var(--blue) 55%, var(--blue-bright) 100%);
    overflow: hidden;
  }
  .header::after {
    content: ""; position: absolute; top: -20px; right: 120px; width: 60px; height: 170px;
    background: rgba(255,255,255,.18); transform: skewX(-25deg);
  }
  .header h1 {
    position: absolute; left: 40px; top: 12px;
    font-family: "Roboto Condensed", sans-serif; font-style: italic; font-weight: 800;
    font-size: 64px; color: var(--white); line-height: 1;
  }
  .header p {
    position: absolute; left: 40px; top: 78px;
    font-weight: 700; font-style: italic; font-size: 30px; color: var(--white);
  }

  /* map & brand */
  .world-map {
    position: absolute; left: 60px; top: 140px; width: 730px; height: 300px;
    background: radial-gradient(ellipse at 50% 50%, #c9ccd2 0%, #e4e6ea 60%, var(--paper) 100%);
    border-radius: 40px; opacity: .9;
  }
  .brand { position: absolute; left: 0; top: 290px; width: 100%; text-align: center; }
  .brand-name {
    display: inline-flex; align-items: center; gap: 16px;
    font-family: "Roboto Condensed", sans-serif; font-weight: 700;
    font-size: 74px; color: var(--blue); letter-spacing: 1px;
  }
  .brand-name .mark { width: 34px; height: 34px; background: var(--blue); display: inline-block; }
  .brand-tagline { margin-top: 6px; font-style: italic; font-weight: 700; font-size: 30px; color: var(--ink); }

  /* features */
  .feature {
    position: absolute; font-weight: 700; font-style: italic; color: var(--ink);
    display: flex; align-items: center; gap: 6px; white-space: nowrap;
  }
  .feature svg { width: 26px; height: 14px; flex: none; }
  .f1 { left: 70px;  top: 462px; font-size: 22px; }
  .f2 { left: 420px; top: 446px; font-size: 17px; }
  .f3 { left: 320px; top: 498px; font-size: 18px; }
  .f4 { left: 95px;  top: 530px; font-size: 22px; }
  .f5 { left: 455px; top: 542px; font-size: 26px; }
  .f6 { left: 70px;  top: 575px; font-size: 16px; }
  .f7 { left: 330px; top: 590px; font-size: 20px; }
  .f8 { left: 620px; top: 608px; font-size: 12px; }

  /* call */
  .call-badge {
    position: absolute; left: 25px; top: 690px; width: 140px; height: 140px; border-radius: 50%;
    background: radial-gradient(circle at 40% 35%, #ff3b3b, var(--red) 55%, var(--red-dark));
    border: 5px solid var(--white); box-shadow: 0 3px 8px rgba(0,0,0,.3);
    color: var(--white); font-family: "Roboto Condensed", sans-serif; font-weight: 800; font-style: italic;
    font-size: 44px; line-height: .95; padding: 26px 0 0 22px;
  }
  .call-badge svg { position: absolute; right: 16px; bottom: 20px; width: 34px; height: 34px; }
  .call-text { position: absolute; left: 200px; top: 720px; }
  .call-text p { font-weight: 700; font-size: 24px; }
  .call-text .phone {
    margin-top: 8px; font-family: "Roboto Condensed", sans-serif; font-style: italic; font-weight: 800;
    font-size: 50px; color: var(--red);
  }

  /* promo */
  .promo {
    position: absolute; left: 0; top: 850px; width: 100%; height: 290px;
    background: linear-gradient(180deg, var(--blue) 0%, var(--blue-deep) 100%);
    color: var(--white);
  }
  .promo-title {
    height: 66px; padding: 10px 0 0 110px;
    background: linear-gradient(90deg, var(--blue-bright), var(--blue));
    font-weight: 700; font-size: 46px; line-height: 1;
  }
  .promo-body { padding: 12px 0 0 40px; }
  .promo-body .lead { font-weight: 700; font-size: 22px; line-height: 1.2; width: 500px; }
  .promo-body .facts {
    margin-top: 6px; font-family: "Roboto Condensed", sans-serif; font-weight: 700;
    font-size: 36px; line-height: 1.02;
  }
  .burst { position: absolute; right: 30px; top: 70px; width: 270px; height: 210px; }
  .footer-band {
    position: absolute; left: 0; top: 1140px; width: 100%; height: 60px;
    background: linear-gradient(180deg, #e8eaed, var(--grey));
  }
</style>
</head>
<body>
<main class="flyer">
  <header class="header">
    <h1>Our focus</h1>
    <p>is on the commercial shipping customer</p>
  </header>

  <div class="world-map" role="img" aria-label="Dotted world map in light grey"></div>

  <section class="brand">
    <div class="brand-name"><span class="mark"></span>MIDWAY SWIFTLINE</div>
    <div class="brand-tagline">every package is a priority</div>
  </section>

  <svg width="0" height="0" style="position:absolute">
    <defs>
      <symbol id="arrow" viewBox="0 0 26 14"><path d="M0 3h16V0l10 7-10 7v-3H0z" fill="#1565c0"/></symbol>
    </defs>
  </svg>

  <div class="feature f1">Overnight courier service <svg><use href="#arrow"/></svg></div>
  <div class="feature f2">Friendly and reliable shipping experience <svg><use href="#arrow"/></svg></div>
  <div class="feature f3">Guaranteed shipment will always arrive when stated <svg><use href="#arrow"/></svg></div>
  <div class="feature f4">No package misplaced <svg><use href="#arrow"/></svg></div>
  <div class="feature f5">No extra fees <svg><use href="#arrow"/></svg></div>
  <div class="feature f6">Traceable freight <svg><use href="#arrow"/></svg></div>
  <div class="feature f7">Web based dispatch <svg><use href="#arrow"/></svg></div>
  <div class="feature f8">On site services <svg><use href="#arrow"/></svg></div>

  <div class="call-badge">Call<br>us
    <svg viewBox="0 0 24 24"><path fill="#fff" d="M6.6 10.8a15 15 0 0 0 6.6 6.6l2.2-2.2c.3-.3.7-.4 1-.2 1.1.4 2.3.6 3.6.6.6 0 1 .4 1 1V20c0 .6-.4 1-1 1C10.6 21 3 13.4 3 4c0-.6.4-1 1-1h3.5c.6 0 1 .4 1 1 0 1.3.2 2.5.6 3.6.1.3 0 .7-.2 1z"/></svg>
  </div>
  <div class="call-text">
    <p>Call us now, because every package is a priority</p>
    <div class="phone">Toll Free 1.877.555.0142</div>
  </div>

  <section class="promo">
    <div class="promo-title">10 dollar triangle</div>
    <div class="promo-body">
      <p class="lead">Ship anywhere between Calgary Lethbridge and Medicine Hat or anywhere point between for just 10 Bucks</p>
      <p class="facts">Max weight 150lbs<br>Guaranteed Overnight<br>G.S.T. extra</p>
    </div>
    <svg class="burst" viewBox="0 0 270 210">
      <polygon fill="#fff" points="135,0 160,40 210,10 205,62 268,60 225,100 268,140 205,145 215,205 160,170 135,210 110,170 55,205 65,145 2,140 45,100 2,60 65,62 60,10 110,40"/>
      <polygon fill="#d8121b" points="135,12 158,50 202,24 198,70 252,70 215,102 252,134 198,136 206,188 158,160 135,198 112,160 64,188 72,136 18,134 55,102 18,70 72,70 68,24 112,50"/>
      <g transform="rotate(-12 135 105)" fill="#fff" font-family="Roboto Condensed, sans-serif" font-weight="800" font-style="italic" text-anchor="middle">
        <text x="135" y="95" font-size="44">NO</text>
        <text x="135" y="128" font-size="36">EXTRA</text>
        <text x="135" y="152" font-size="22">SURCHARGES</text>
      </g>
    </svg>
  </section>
  <div class="footer-band"></div>
</main>
</body>
</html>
```